4th Generation Family Business Needs a New Card Design!

We are a family owned 4th Generation company. We are based in the Sydney, Australia area and we are desperately in need of a more modern and classy card. We are monumental masons who design, supply & erect lasting memorials throughout cemeteries in Sydney. Our customers are normally in a period of grieving. I have attached logo files that will need to be implemented on the card. Company was established 1935. Australian Owned and Operated. Card needs to be designed to PRINTLY.com specification.

Target Market(s)

Our target market is based upon people that a grieving for family members that have passed away. We also deal with alot of companies that own and operate cemeteries.

Industry/Entity Type

Business

Contact Information for Business Card

Oliver Brantley, Operations Manager, 0417552908, oliver@hollowaystoneworks.com.au
Martin Brantley, Director, 0431906627, martin@hollowaystoneworks.com.au
Phone # 02 9634 2258
Website: www.hollowaystoneworks.com.au
Address: Suite 17, 8 Calloway Lane, East Penrose, Sydney NSW 2290

Font styles to use
Serif
Decorative
Script

Requirements
Must have
• Would like to see the logo nicely implemented with a modern design. Embossed lettering would be a nice additive.

```html
<!DOCTYPE html>
<html lang="en">
<head>
<meta charset="utf-8">
<title>Holloway Stoneworks – Business Card</title>
<link href="https://fonts.googleapis.com/css2?family=Lato:wght@300;400;700&display=swap" rel="stylesheet">
<style>
  :root {
    --gold: #e9b92a;
    --ink: #231f20;
    --grey: #6d6e71;
    --paper: #ffffff;
    --slate: #262626;
    --backdrop: #e9e6e2;
    --ghost: #f2f2f2;
  }
  * { box-sizing: border-box; margin: 0; padding: 0; }
  html, body { width: 1200px; height: 960px; overflow: hidden; }
  body {
    background: var(--backdrop);
    font-family: "Lato", sans-serif;
    position: relative;
  }
  .card {
    position: absolute;
    left: 248px;
    width: 704px;
    height: 400px;
    overflow: hidden;
  }
  .card--front { top: 52px; background: var(--paper); }
  .card--back { top: 508px; background: var(--slate); }

  .ghost-name {
    position: absolute;
    right: -10px;
    top: 10px;
    font-size: 150px;
    font-weight: 700;
    color: var(--ghost);
    line-height: 1;
    letter-spacing: -2px;
  }

  .brand {
    position: absolute;
    display: flex;
    align-items: center;
    gap: 12px;
    font-weight: 700;
    letter-spacing: 2px;
    text-transform: uppercase;
  }
  .brand__mark { width: 30px; height: 30px; background: var(--gold); flex: none; }
  .card--front .brand { left: 48px; top: 120px; font-size: 22px; color: var(--ink); }
  .card--back .brand {
    left: 0; right: 0; top: 160px; justify-content: center;
    font-size: 34px; color: #ffffff; gap: 16px;
  }
  .card--back .brand__mark { width: 40px; height: 40px; }

  .person { position: absolute; left: 48px; top: 254px; }
  .person__name { font-size: 24px; font-weight: 700; color: var(--gold); letter-spacing: 0.5px; }
  .person__role { font-size: 18px; color: var(--grey); letter-spacing: 1px; margin-top: 1px; }

  .contact { list-style: none; font-size: 17px; font-weight: 400; color: var(--grey); }
  .contact li { display: flex; align-items: center; gap: 10px; height: 22px; }
  .contact svg { width: 14px; height: 14px; flex: none; }
  .person .contact { margin-top: 10px; }

  .company { position: absolute; left: 418px; top: 252px; }
  .company__name { font-size: 17px; font-weight: 700; color: var(--gold); }
  .company__address { font-size: 17px; font-weight: 300; color: var(--grey); line-height: 22px; font-style: normal; margin-bottom: 8px; }
  .company__address span { display: block; }

  .footer-band { position: absolute; left: 0; bottom: 0; width: 704px; height: 12px; }

  .web-line {
    position: absolute; left: 0; right: 0; top: 326px;
    text-align: center; font-size: 16px; letter-spacing: 3px; color: #ffffff;
  }
  .web-line em { font-style: normal; color: var(--gold); }
</style>
</head>
<body>

<section class="card card--front" aria-label="Card front">
  <div class="ghost-name" aria-hidden="true">Holloway</div>

  <div class="brand">
    <span class="brand__mark"></span>
    <span class="brand__name">Holloway Stoneworks</span>
  </div>

  <div class="person">
    <p class="person__name">Martin Brantley</p>
    <p class="person__role">Director</p>
    <ul class="contact">
      <li>
        <svg viewBox="0 0 14 14" fill="none" stroke="#e9b92a" stroke-width="1.4"><rect x="3.5" y="0.8" width="7" height="12.4" rx="1.2"/><line x1="6" y1="11" x2="8" y2="11"/></svg>
        0431906627
      </li>
      <li>
        <svg viewBox="0 0 14 14" fill="none" stroke="#e9b92a" stroke-width="1.3"><rect x="0.8" y="2.8" width="12.4" height="8.4"/><polyline points="0.8,2.8 7,7.6 13.2,2.8"/></svg>
        martin@hollowaystoneworks.com.au
      </li>
    </ul>
  </div>

  <div class="company">
    <p class="company__name">Holloway Stoneworks</p>
    <address class="company__address">
      <span>Suite 17, 8 Calloway Lane</span>
      <span>East Penrose, Sydney NSW 2290</span>
    </address>
    <ul class="contact">
      <li>
        <svg viewBox="0 0 14 14" fill="#e9b92a"><path d="M3 1 L5.5 1 L6 4.5 L4.6 5.6 Q6 8.8 8.6 9.6 L9.6 8.2 L13 8.8 L13 11.4 Q12.6 13 11 13 Q2 12 1 3 Q1.2 1.2 3 1 Z"/></svg>
        02 9634 2258
      </li>
      <li>
        <svg viewBox="0 0 14 14" fill="none" stroke="#e9b92a" stroke-width="1.1"><circle cx="7" cy="7" r="6"/><ellipse cx="7" cy="7" rx="2.6" ry="6"/><line x1="1" y1="7" x2="13" y2="7"/></svg>
        www.hollowaystoneworks.com.au
      </li>
    </ul>
  </div>

  <svg class="footer-band" viewBox="0 0 704 12" preserveAspectRatio="none" aria-hidden="true">
    <polygon points="0,0 362,0 352,12 0,12" fill="#e9b92a"/>
    <polygon points="366,0 704,0 704,12 356,12" fill="#231f20"/>
  </svg>
</section>

<section class="card card--back" aria-label="Card back">
  <div class="brand">
    <span class="brand__mark"></span>
    <span class="brand__name">Holloway Stoneworks</span>
  </div>
  <p class="web-line">www.<em>hollowaystoneworks</em>.com.au</p>
</section>

</body>
</html>
```